Business card design for strategy and management consulting company. Would like to have a clean and professional business card, based on the attached logo. The company is a strategy and management consulting company focusing on sustainable business modlels based on economic, social and environmental market opportunities. Preferably the logo should be included on both sides of the design.

Industry/Entity Type

Business

Contact Information for Business Card

Halvor Brekkeli, CEO/Management consultant
halvor.brekkeli@morvikpartners.example
Mob: +47 936 28 417
Office: Lyngvedens gate 14, pb 312 sentrum, N-0158 Oslo Norway

Requirements
Must have
• Include attached logo
Nice to have
• Would like to have the logo on both sides
Should not have
• Many colours.

```html
<!DOCTYPE html>
<html lang="en">
<head>
<meta charset="utf-8">
<title>Morvik business card</title>
<link href="https://fonts.googleapis.com/css2?family=Work+Sans:wght@400;600;700&display=swap" rel="stylesheet">
<style>
  :root {
    --backdrop: #2b2b2b;
    --brand-yellow: #f7e417;
    --card-dark: #1e1e1e;
    --ink-dark: #1a1a1a;
    --ink-light: #f2f2f2;
    --ink-muted: #d6d6d6;
  }
  * { box-sizing: border-box; margin: 0; padding: 0; }
  html, body {
    width: 1200px; height: 900px; overflow: hidden;
    background: var(--backdrop);
    font-family: "Work Sans", Arial, sans-serif;
  }
  .canvas { position: relative; width: 1200px; height: 900px; }
  .card {
    position: absolute; left: 250px; width: 700px; height: 400px;
    box-shadow: 0 14px 30px rgba(0,0,0,0.45);
    overflow: hidden;
  }
  .card-front {
    top: 40px; background: var(--brand-yellow);
    display: flex; align-items: center; justify-content: center;
  }
  .card-back { top: 470px; background: var(--card-dark); }

  .wordmark { font-weight: 700; letter-spacing: -1px; line-height: 1; white-space: nowrap; }
  .card-front .wordmark { font-size: 110px; color: var(--ink-dark); }

  .back-logo {
    position: absolute; left: 55px; top: 128px; width: 250px;
    display: flex; justify-content: center;
  }
  .card-back .wordmark { font-size: 68px; color: var(--ink-light); }

  .divider {
    position: absolute; left: 325px; top: 112px; width: 2px; height: 160px;
    background: var(--ink-muted);
  }
  .contact {
    position: absolute; left: 345px; top: 112px; width: 330px;
    color: var(--ink-muted); font-size: 15px; line-height: 1.5;
  }
  .contact-name {
    color: var(--brand-yellow); font-weight: 700; font-size: 26px; line-height: 1.1;
  }
  .contact-role { margin-bottom: 4px; }
  .contact-line { display: flex; align-items: center; gap: 9px; white-space: nowrap; }
  .contact-line svg { width: 12px; height: 12px; flex: none; }
  .contact-email { font-size: 13.5px; }
</style>
</head>
<body>
<main class="canvas">
  <section class="card card-front" aria-label="Card front">
    <span class="wordmark">Morvik</span>
  </section>

  <section class="card card-back" aria-label="Card back">
    <div class="back-logo"><span class="wordmark">Morvik</span></div>
    <div class="divider"></div>
    <div class="contact">
      <p class="contact-name">Halvor Brekkeli</p>
      <p class="contact-role">CEO/Management consultant</p>
      <p>Lyngvedens gate 14,</p>
      <p>pb 312 sentrum, Oslo Norway</p>
      <p class="contact-line">
        <svg viewBox="0 0 12 12" aria-hidden="true"><rect x="3" y="0.8" width="6" height="10.4" rx="1.2" fill="none" stroke="#f7e417" stroke-width="1.4"/><line x1="5" y1="9" x2="7" y2="9" stroke="#f7e417" stroke-width="1.2"/></svg>
        <span>+47 936 28 417</span>
      </p>
      <p class="contact-line">
        <svg viewBox="0 0 12 12" aria-hidden="true"><rect x="0.8" y="2.5" width="10.4" height="7" fill="none" stroke="#f7e417" stroke-width="1.4"/><polyline points="1,3 6,7 11,3" fill="none" stroke="#f7e417" stroke-width="1.2"/></svg>
        <span class="contact-email">halvor.brekkeli@morvikpartners.example</span>
      </p>
    </div>
  </section>
</main>
</body>
</html>
```